Worksheet for a seminar - wheel of wellbeing

I need a 1 page worksheet for a course I am running next week.
1. The worksheet is based is designed to tie into Valdoric who use 4 colours per specific quadrants - Blue top left, Yellow top right, Green bottom left, Red bottom right. As this is designed to be written and to be printed, it may need to be pale colours however I am open to the correct colours with the image on top if necessary

2. The wellbeing wheel needs to be a design of it's own as it will be used in other things. I would like to have a format for the base wheel that can be changed by me (Only the title names)

3. I have provided the 2 business logo's - these down need to be too big

I hope this helps.

Target Market(s)

Corporate managers and staff - worksheet being used in a workshop

Industry/Entity Type

Wheel

Colors

Designer to choose colors to be used in the design.

Requirements
Must have
• A professional looking wheel that can be used for other purposes. I want to be able to change the 'pie' titles. I will also require a A4 size of the wheel with blank spaces for titles
Nice to have
• A modern feel

```html
<!DOCTYPE html>
<html lang="en">
<head>
<meta charset="utf-8">
<title>A Whole Brain Approach – Worksheet</title>
<link href="https://fonts.googleapis.com/css2?family=Open+Sans:wght@400;600;700&family=PT+Sans+Narrow:wght@400;700&family=Roboto+Slab:wght@400;500;600&display=swap" rel="stylesheet">
<style>
  :root{
    --backdrop:#e8e5e0;
    --paper:#ffffff;
    --navy:#0d2a4a;
    --ink:#3e3e3e;
    --heading-blue:#1a7cc1;
    --rule:#9a9a9a;
    --ring:#b9dcf2;
    --seg-physical:#1fb5cf;
    --seg-emotional:#e8892b;
    --seg-spiritual:#8e2a6b;
    --seg-love:#d91e4b;
    --seg-family:#6db545;
    --seg-social:#0a5f9e;
    --seg-personal:#e8769a;
    --seg-business:#8088c2;
    --quad-a:#0e8fd0;
    --quad-d:#fdea1f;
    --quad-b:#35b34a;
    --quad-c:#ef5440;
    --pill-green:#35b34a;
    --pill-red:#d81e4c;
    --pill-pink:#eb4370;
    --band:#163a5a;
  }
  *{box-sizing:border-box;margin:0;padding:0}
  html,body{width:1200px;height:1200px;overflow:hidden;background:var(--backdrop)}
  .sheet{
    position:absolute;left:190px;top:20px;width:887px;height:1255px;
    background:var(--paper);transform:scale(.924);transform-origin:0 0;
    font-family:"Open Sans",sans-serif;color:var(--ink);
    box-shadow:0 4px 18px rgba(0,0,0,.18);
  }
  .abs{position:absolute}
  .brand{left:292px;top:21px;display:flex;align-items:center;gap:18px}
  .brand-dot{width:118px;height:118px;border-radius:50%;background:var(--seg-physical)}
  .brand-name{font-family:"Roboto Slab",serif;font-weight:500;font-size:30px;line-height:29px;color:#3a3a3a}
  .title{left:0;width:887px;top:158px;text-align:center;font-family:"Roboto Slab",serif;font-size:56px;font-weight:400;color:#444;letter-spacing:.5px}
  .title strong{font-weight:500;color:var(--navy)}
  .rule{left:40px;width:807px;top:233px;height:1px;background:var(--rule)}
  .col-head{text-align:center;width:400px}
  .col-head h2{font-size:27px;font-weight:700;color:var(--heading-blue);line-height:34px}
  .col-head p{font-size:21px;color:#444;line-height:28px}
  .wheel{overflow:visible}
  .seg-label{font-family:"Open Sans",sans-serif;font-weight:700;font-size:11px;fill:#fff}
  .quad-label{font-family:"Open Sans",sans-serif;font-weight:700;font-size:10px;fill:#fff}
  .quad-label.dark{fill:#222}
  .mode{font-family:"Open Sans",sans-serif;font-size:12px;fill:#222}
  .corner{font-family:"Open Sans",sans-serif;font-weight:700;font-size:18px;fill:#111}
  .field{font-family:"Open Sans",sans-serif;font-size:15px;color:#222;display:flex;align-items:flex-end;gap:26px}
  .field .line{border-bottom:1px solid #888;height:1px;flex:1;margin-bottom:4px}
  .section{font-size:23px;font-weight:700;color:var(--heading-blue)}
  .small{font-family:"PT Sans Narrow",sans-serif;font-size:16px;color:#222}
  .pill{width:354px;height:44px;border-radius:22px;overflow:hidden;box-shadow:0 2px 4px rgba(0,0,0,.25),inset 0 0 0 1px rgba(0,0,0,.08)}
  .pill.action{background:linear-gradient(90deg,var(--pill-green) 0 250px,#fff 250px)}
  .pill.red{background:var(--pill-red)}
  .pill.pink{background:var(--pill-pink)}
  .question{font-family:"PT Sans Narrow",sans-serif;font-size:15px;color:#222}
  .question.tight{font-size:13px}
  .partner{font-family:"Open Sans",sans-serif;font-weight:700;font-size:17px;display:flex;align-items:center;gap:7px}
  .partner i{display:block;width:14px;height:14px;border-radius:50%}
  .contact{font-size:15px;color:#222;display:flex;align-items:center;gap:10px}
  .contact.web{letter-spacing:3.6px;font-size:13px}
  .band{left:0;bottom:0;width:887px;height:18px;background:var(--band)}
</style>
</head>
<body>
<div class="sheet">

  <header>
    <div class="abs brand">
      <span class="brand-dot"></span>
      <span class="brand-name">Thrive<br>Circle</span>
    </div>
    <h1 class="abs title">A whole <strong>BRAIN APPROACH</strong></h1>
    <div class="abs rule"></div>
  </header>

  <div class="abs col-head" style="left:9px;top:254px">
    <h2>Assess :</h2>
    <p>Where are you now ?</p>
  </div>
  <div class="abs col-head" style="left:457px;top:252px">
    <h2>Outcomes Goals</h2>
    <p>Where do you want to be ?</p>
  </div>

  <!-- Life areas wheel -->
  <svg class="abs wheel" style="left:0;top:0" width="887" height="1255" viewBox="0 0 887 1255">
    <g transform="translate(221 516)">
      <circle r="158" fill="none" stroke="var(--ring)" stroke-width="5"/>
      <g stroke="#fff" stroke-width="6">
        <path d="M0 0L0 -155A155 155 0 0 1 109.6 -109.6Z" fill="var(--seg-physical)"/>
        <path d="M0 0L109.6 -109.6A155 155 0 0 1 155 0Z" fill="var(--seg-emotional)"/>
        <path d="M0 0L155 0A155 155 0 0 1 109.6 109.6Z" fill="var(--seg-spiritual)"/>
        <path d="M0 0L109.6 109.6A155 155 0 0 1 0 155Z" fill="var(--seg-love)"/>
        <path d="M0 0L0 155A155 155 0 0 1 -109.6 109.6Z" fill="var(--seg-family)"/>
        <path d="M0 0L-109.6 109.6A155 155 0 0 1 -155 0Z" fill="var(--seg-social)"/>
        <path d="M0 0L-155 0A155 155 0 0 1 -109.6 -109.6Z" fill="var(--seg-personal)"/>
        <path d="M0 0L-109.6 -109.6A155 155 0 0 1 0 -155Z" fill="var(--seg-business)"/>
      </g>
      <circle r="62" fill="var(--ring)"/>
      <circle r="55" fill="#fff" stroke="#e2e2e2" stroke-width="2"/>
      <g text-anchor="middle" class="seg-label">
        <text class="seg-label" x="-39" y="-100">BUSINESS</text>
        <text class="seg-label" x="-39" y="-86">CAREER</text>
        <text class="seg-label" x="-39" y="-72">STUDY</text>
        <text class="seg-label" x="44" y="-89">PHYSICAL</text>
        <text class="seg-label" x="44" y="-75">HEALTH</text>
        <text class="seg-label" x="104" y="-31">EMOTIONAL</text>
        <text class="seg-label" x="104" y="-17">HEALTH</text>
        <text class="seg-label" x="105" y="48">SPRITUAL</text>
        <text class="seg-label" x="49" y="103">LOVE</text>
        <text class="seg-label" x="49" y="117">RELATIONSHIP</text>
        <text class="seg-label" x="-42" y="116">FAMILY</text>
        <text class="seg-label" x="-105" y="48">SOCIAL</text>
        <text class="seg-label" x="-106" y="-31">PERSONAL</text>
        <text class="seg-label" x="-106" y="-17">GROWTH</text>
      </g>
    </g>

    <!-- Thinking preferences wheel -->
    <g transform="translate(666 508)">
      <circle r="158" fill="none" stroke="var(--ring)" stroke-width="5"/>
      <path d="M0 0L-155 0A155 155 0 0 1 0 -155Z" fill="var(--quad-a)"/>
      <path d="M0 0L0 -155A155 155 0 0 1 155 0Z" fill="var(--quad-d)"/>
      <path d="M0 0L155 0A155 155 0 0 1 0 155Z" fill="var(--quad-c)"/>
      <path d="M0 0L0 155A155 155 0 0 1 -155 0Z" fill="var(--quad-b)"/>
      <path d="M0 -156V156M-156 0H156" stroke="#fff" stroke-width="8"/>
      <circle r="62" fill="var(--ring)"/>
      <circle r="55" fill="#fff" stroke="#e2e2e2" stroke-width="2"/>
      <g>
        <text class="quad-label" x="-112" y="-90">LOGICAL</text>
        <text class="quad-label" x="-112" y="-77">ANALYTICAL</text>
        <text class="quad-label" x="-112" y="-64">FACT BASED</text>
        <text class="quad-label" x="-112" y="-51">QUANTITATIVE</text>
        <text class="quad-label dark" x="50" y="-90">HOLISTIC</text>
        <text class="quad-label dark" x="50" y="-77">INTUITIVE</text>
        <text class="quad-label dark" x="50" y="-64">INTEGRATING</text>
        <text class="quad-label dark" x="50" y="-51">SYNTHESIZING</text>
        <text class="quad-label" x="-108" y="62">ORGANIZED</text>
        <text class="quad-label" x="-108" y="75">SEQUENTIAL</text>
        <text class="quad-label" x="-108" y="88">PLANNED</text>
        <text class="quad-label" x="-108" y="101">DETAILED</text>
        <text class="quad-label" x="52" y="64">INTEPERSONAL</text>
        <text class="quad-label" x="52" y="77">FEELING BASED</text>
        <text class="quad-label" x="52" y="90">KINESTHETIC</text>
        <text class="quad-label" x="52" y="103">EMOTIONAL</text>
      </g>
      <text class="mode" text-anchor="middle" y="-172">CEREBRAL MODE</text>
      <text class="mode" text-anchor="middle" y="191">LIMBIC MODE</text>
      <text class="mode" text-anchor="middle" transform="translate(-170 0) rotate(-90)">LEFT MODE</text>
      <text class="mode" text-anchor="middle" transform="translate(170 0) rotate(90)">RIGHT MODE</text>
      <text class="corner" x="-172" y="-138">A</text>
      <text class="corner" x="151" y="-138">D</text>
      <text class="corner" x="-175" y="164">B</text>
      <text class="corner" x="152" y="164">C</text>
    </g>
  </svg>

  <div class="abs field" style="left:40px;top:736px;width:368px">Date :<span class="line"></span></div>
  <div class="abs field" style="left:492px;top:742px;width:357px">Date achieved by :<span class="line"></span></div>

  <!-- Action plan -->
  <h3 class="abs section" style="left:41px;top:776px">Action Plan :</h3>
  <span class="abs small" style="left:41px;top:811px">Action</span>
  <span class="abs small" style="left:314px;top:811px">when</span>
  <div class="abs pill action" style="left:40px;top:843px"></div>
  <div class="abs pill action" style="left:40px;top:929px"></div>
  <div class="abs pill action" style="left:40px;top:1011px"></div>
  <div class="abs pill action" style="left:40px;top:1096px"></div>

  <!-- Reflect -->
  <h3 class="abs section" style="left:490px;top:776px">Reflect :</h3>
  <span class="abs question" style="left:493px;top:811px">Are there any surprises in your wheel ?</span>
  <div class="abs pill red" style="left:492px;top:843px"></div>
  <span class="abs question tight" style="left:493px;top:900px">What wellbeing gaps stand out as being most important ?</span>
  <div class="abs pill pink" style="left:493px;top:929px"></div>
  <span class="abs question" style="left:493px;top:985px">How do you feel about it ?</span>
  <div class="abs pill red" style="left:494px;top:1011px"></div>
  <span class="abs question" style="left:493px;top:1070px">How might this affect you homelife/ worklift ?</span>
  <div class="abs pill pink" style="left:492px;top:1096px"></div>

  <!-- Footer -->
  <footer>
    <div class="abs partner" style="left:54px;top:1193px;color:var(--pill-green)"><i style="background:var(--pill-green)"></i>Brightpath Ventures</div>
    <div class="abs partner" style="left:54px;top:1193px;transform:translateX(228px);color:#3bb3a3">Staffbloom</div>
    <div class="abs contact" style="left:493px;top:1170px">
      <svg width="18" height="13" viewBox="0 0 18 13"><rect x="1" y="1" width="16" height="11" fill="none" stroke="var(--navy)" stroke-width="2"/><path d="M1 1L9 7L17 1" fill="none" stroke="var(--navy)" stroke-width="2"/></svg>
      hello@thrivecircle.example
    </div>
    <div class="abs contact web" style="left:493px;top:1199px">
      <svg width="18" height="18" viewBox="0 0 18 18"><circle cx="9" cy="9" r="7.5" fill="none" stroke="var(--navy)" stroke-width="1.6"/><ellipse cx="9" cy="9" rx="3.2" ry="7.5" fill="none" stroke="var(--navy)" stroke-width="1.4"/><path d="M1.5 9H16.5" stroke="var(--navy)" stroke-width="1.4"/></svg>
      www.thrivecircle.example
    </div>
    <div class="abs band"></div>
  </footer>

</div>
</body>
</html>
```